Online-Marketing Material für medizinischen Online Ratgeber
Zielgruppe
Die Welt der Thoraxmedizin kann komplex und verwirrend sein. Orvena Linde steht für kompetente Beratung und verlässliche Informationen rund um das Thema Thoraxerkrankungen – entstanden aus dem Wunsch, umfassende Informationen zur Verfügung zu stellen Ob Lungenkrebs, Asthma, COPD oder Schlafapnoe – wir bringen Klarheit in alle Aspekte der ThoraxmedizinThorax Schweiz ist nicht nur eine Informationsplattform, sondern auch eine Gemeinschaft, in der jeder willkommen und eingeladen ist, Fragen zu stellen, sein Wissen zu erweitern und zu teilen.
Aufgabenstellung
Orvena Linde ist ein online Ratgeber im Bereich der thorax Erkrankungen. wir wollen mit dem facebook Auftritt die Webseite ergänzen.Wir benötigen für facebook ein Profilbanner (1200x630), ein Profilbild 800x800) sowie einen Entwurf für ein posting(800x800). Die Farben die verwendet werden solltenund das Logo von orvena linde habe ich im Anhang beigefügt.Ich bedanke mich schon jetzt für Ihre Mühe und freue mich auf Ihre Entwürfe.

```html
<!DOCTYPE html>
<html lang="de">
<head>
<meta charset="utf-8">
<title>Orvena Linde – Social-Media-Vorlagen</title>
<link rel="stylesheet" href="https://fonts.googleapis.com/css2?family=Bebas+Neue&family=Roboto+Condensed:wght@700&display=swap">
<style>
  :root {
    --canvas: #ffffff;
    --navy: #163c6c;
    --brand-blue: #0a95d5;
    --ring-blue: #1b98d8;
    --sky-light: #bcdcec;
    --sky-mid: #a9cfe2;
    --white: #ffffff;
  }
  * { margin: 0; padding: 0; box-sizing: border-box; }
  html, body { width: 1200px; height: 848px; overflow: hidden; background: var(--canvas); }
  .artboard { position: relative; width: 1200px; height: 848px; }

  /* Profile banner */
  .banner {
    position: absolute; left: 239px; top: 73px; width: 681px; height: 357px;
    overflow: hidden;
  }
  .banner-photo {
    position: absolute; inset: 0;
    background: linear-gradient(120deg, var(--sky-light) 0%, var(--sky-mid) 100%);
  }
  .banner-headline {
    position: absolute; left: 0; top: 0;
    font-family: "Bebas Neue", sans-serif; font-weight: 400;
    font-size: 58px; line-height: 54px; color: var(--navy);
    letter-spacing: 0.2px;
  }
  .banner-headline span { position: absolute; white-space: nowrap; }
  .line-1 { left: 63px; top: 95px; }
  .line-2 { left: 100px; top: 149px; }
  .line-3 { left: 54px; top: 202px; }

  /* Profile picture */
  .profile-badge {
    position: absolute; left: 297px; top: 358px; width: 168px; height: 168px;
    border-radius: 50%; background: var(--white);
    border: 4px solid var(--ring-blue);
    display: flex; align-items: center; justify-content: center;
  }
  .profile-name {
    font-family: "Roboto Condensed", sans-serif; font-weight: 700;
    font-size: 25px; line-height: 24px; color: var(--navy);
    text-align: center; text-transform: uppercase;
  }

  /* Post */
  .post {
    position: absolute; left: 534px; top: 464px; width: 332px; height: 332px;
    background: var(--brand-blue);
    font-family: "Roboto Condensed", sans-serif; font-weight: 700;
    text-align: center; color: var(--white);
  }
  .post-tag {
    position: absolute; left: 85px; top: 62px; width: 154px; height: 28px;
    background: var(--navy); font-size: 19px; line-height: 28px;
  }
  .post-statement {
    position: absolute; left: 0; right: 0; top: 98px;
    font-size: 45px; line-height: 42px; letter-spacing: -0.3px;
  }
  .post-statement .highlight { color: var(--navy); }
  .post-brand {
    position: absolute; left: 0; right: 0; top: 296px;
    font-size: 17px; line-height: 20px; letter-spacing: 0.3px; text-transform: uppercase;
  }
</style>
</head>
<body>
<main class="artboard">
  <section class="banner">
    <div class="banner-photo" role="img" aria-label="Foto: Papierlunge in Rosa und Weiß mit Stethoskop auf hellblauem Hintergrund"></div>
    <h1 class="banner-headline">
      <span class="line-1">Ihr Ratgeber</span>
      <span class="line-2">für Thorax-</span>
      <span class="line-3">Patienten</span>
    </h1>
  </section>

  <div class="profile-badge">
    <p class="profile-name">Orvena<br>Linde</p>
  </div>

  <section class="post">
    <p class="post-tag">Schon gewußt?</p>
    <p class="post-statement">Lorem ipsum<br>est durum <span class="highlight">80%</span><br>fertet dolu.</p>
    <p class="post-brand">Orvena Linde</p>
  </section>
</main>
</body>
</html>
```